Quillfern Nightclub Flyer (Updated)

Flyer for facebook, square is fine, or rectangular. Here is the text:
QUILLFERN
Nightclub + Lounge
presents

SPLIT DECK WEDNESDAY
Nov 29 2018

CLUB FLOOR:
GORDY B2B RALPH
THEODORE BRUSKVIK

LOUNGE:
OTIS B2B HALF TIDE
COPPER FENWICK

Powered by HALVERN Acoustics
4716 Larchmere Avenue 21+ 9pm-2am
quillfernvenue-example.com for VIP booth inquiries

Target Market(s)

Nightclub

Industry/Entity Type

Night Club

Font styles to use
Sans Serif

Colors

Designer to choose colors to be used in the design.

Requirements
Must have
• All the text listed, and plz keep the theme of the attached files. We want to stay consistent with the Quillfern brand
Nice to have
• Try to stay with the theme from the attachments
Should not have
• Dont' stray to far from the general theme we have from the attachments

```html
<!DOCTYPE html>
<html lang="en">
<head>
<meta charset="utf-8">
<title>Quillfern Nightclub – Split Deck Wednesday</title>
<link rel="stylesheet" href="https://fonts.googleapis.com/css2?family=Marcellus&family=Questrial&family=Montserrat:wght@700&display=swap">
<style>
  :root {
    --page: #ffffff;
    --ink: #231f20;
    --olive-gold: #d3cf6e;
    --copper-light: #e2a96a;
    --copper-dark: #a86a36;
    --wordmark-grey: #6e6e6e;
    --text-light: #f2f2f2;
    --rule: #5a4a35;
  }
  html, body {
    margin: 0;
    width: 1200px;
    height: 1200px;
    overflow: hidden;
    background: var(--page);
  }
  .flyer {
    position: absolute;
    left: 95px;
    top: 312px;
    width: 1041px;
    height: 586px;
    background: var(--ink);
    overflow: hidden;
    font-family: "Questrial", sans-serif;
    color: var(--text-light);
  }
  .ornament {
    position: absolute;
    inset: 0;
    width: 100%;
    height: 100%;
  }
  .line {
    position: absolute;
    margin: 0;
    line-height: 1;
    white-space: nowrap;
  }
  .centered {
    left: 0;
    width: 100%;
    text-align: center;
  }
  .brand-dot {
    position: absolute;
    left: 473px;
    top: 32px;
    width: 96px;
    height: 96px;
    border-radius: 50%;
    background: var(--olive-gold);
  }
  .brand-name {
    top: 142px;
    font-family: "Marcellus", serif;
    font-size: 52px;
    color: var(--wordmark-grey);
    letter-spacing: 1px;
  }
  .brand-tagline {
    top: 198px;
    font-size: 10.5px;
    letter-spacing: 2.4px;
    color: #9a9a9a;
  }
  .presents {
    top: 232px;
    font-size: 19px;
  }
  .event-title {
    top: 266px;
    font-family: "Marcellus", serif;
    font-size: 54px;
    color: var(--olive-gold);
  }
  .event-date {
    top: 329px;
    font-size: 30px;
    letter-spacing: 0.5px;
  }
  .lineup {
    position: absolute;
    top: 394px;
    width: 260px;
  }
  .lineup.club-floor { left: 324px; }
  .lineup.lounge { left: 591px; }
  .lineup h2 {
    margin: 0 0 8px;
    font-family: "Montserrat", sans-serif;
    font-weight: 700;
    font-size: 14.5px;
    color: var(--olive-gold);
    line-height: 1;
  }
  .lineup p {
    margin: 0 0 10px;
    font-size: 15.5px;
    line-height: 1;
  }
  .credits {
    top: 493px;
    font-size: 10.5px;
    line-height: 14px;
  }
  .credits strong {
    font-family: "Montserrat", sans-serif;
    font-weight: 700;
    color: var(--olive-gold);
  }
  .divider {
    position: absolute;
    left: 319px;
    top: 551px;
    width: 463px;
    height: 1px;
    background: var(--rule);
  }
  .booking {
    top: 559px;
    font-size: 11px;
  }
  .booking .site { color: var(--olive-gold); }
</style>
</head>
<body>
  <main class="flyer">
    <svg class="ornament" viewBox="0 0 1041 586" aria-hidden="false">
      <defs>
        <radialGradient id="copper-glow" cx="50%" cy="50%" r="50%">
          <stop offset="0%" stop-color="#b9773f"/>
          <stop offset="70%" stop-color="#d9a062"/>
          <stop offset="100%" stop-color="#a86a36"/>
        </radialGradient>
      </defs>
      <g role="img" aria-label="Copper mandala ornament, upper right corner">
        <circle cx="1062" cy="147" r="290" fill="url(#copper-glow)" opacity="0.85"/>
      </g>
      <g role="img" aria-label="Copper mandala ornament, lower left corner">
        <circle cx="-8" cy="515" r="285" fill="url(#copper-glow)" opacity="0.85"/>
      </g>
    </svg>

    <div class="brand-dot"></div>
    <h1 class="line centered brand-name">QUILLFERN</h1>
    <p class="line centered brand-tagline">NIGHTCLUB + LOUNGE</p>

    <p class="line centered presents">PRESENTS</p>
    <h2 class="line centered event-title">Split Deck Wednesday</h2>
    <p class="line centered event-date">NOV 29 2018</p>

    <section class="lineup club-floor">
      <h2>CLUB FLOOR:</h2>
      <p>GORDY B2B RALPH</p>
      <p>THEODORE BRUSKVIK</p>
    </section>
    <section class="lineup lounge">
      <h2>LOUNGE:</h2>
      <p>OTIS B2B HALF TIDE</p>
      <p>COPPER FENWICK</p>
    </section>

    <p class="line centered credits">POWERED BY<br><strong>HALVERN ACOUSTICS</strong> 4716 LARCHMERE AVENUE 21+<br>9PM-2AM</p>

    <div class="divider"></div>
    <p class="line centered booking"><span class="site">QUILLFERNVENUE-EXAMPLE.COM</span> FOR VIP BOOTH INQUIRIES</p>
  </main>
</body>
</html>
```